Stationary Suite for Aussie Law Firm

We are a small law firm operating out of Albany, Western Australia. We have a logo, which we love and was the winner of a ArtFolioHub contest last year.
We require a suite of business stationary products incorporating our logo and contact details. These should be:
1. Letterhead (A4)
The letterhead should incorporate the following information in addition to the logo:
ABN 38 402 917 265 (this is our Australian Business Number)
Petra Lusk atf The PJL Family Trust t/as Kestrel Bay Law & Settlements (legal name of the business)
Address: Harwood Chambers, Tilbury Lane, Albany
Postal Address: PO Box 8127, Albany WA 6332
Telephone: 0461 907 352
Facsimile: 08 9736 2091
Email: info@kestrelbaylaw.com.au
Website: www.kestrelbaylaw.com.au
2. Business Card (90mm x 55mm)
I've attached my current business card layout just for your information.
The front of the business card should include the following information in addition to the logo:
Petra Lusk
Director & Principal Solicitor
Telephone: 0461 907 352
Facsimile: 08 9736 2091
Email: petra@kestrelbaylaw.com.au
The back of the card should be similar to the back of my existing card, but should only have the logo in white and the address of our website (www.kestrelbaylaw.com.au)
3. Email signature block
This should include the same information as the front of the business card.
4. With Compliments slip (DL size)
The With Compliments slip should include the same information as the Letterhead.
5. Banner (830mm x 2000mm)
We need a banner designed for use at marketing events. This should include our website details and logo - other than that you have fairly free reign with the design.
6. Flyer (DL)
We need a flyer setting out our services and main contact details for use at marketing events. The details to be included are:
Telephone: 0461 907 352
Web: www.kestrelbaylaw.com.au
Areas of law:
Wills & Estate Planning
Probate & Letters of Administration
Property Law & Conveyancing
General Commercial Law
Business Law
Style guide:
Please look at our website for an idea as to the style of designs we are looking for - www.kestrelbaylaw.com.au. The design should be modern, sharp and professional.
Colours:
The CMYK details for the colours in our logo are:
Light Blue C72 M5 Y0 K0
Dark Blue C97 M72 Y16 K30
Edit 31/7/2014
I have added a couple of photos that we have used on our website, and additional photos. These are from our local area, so feel free to use these in your designs or to inform them.
- Calibri, Century Gothic

```html
<!DOCTYPE html>
<html lang="en">
<head>
<meta charset="utf-8">
<title>Kestrel Bay Law &amp; Settlements – Stationery Suite</title>
<link rel="stylesheet" href="https://fonts.googleapis.com/css2?family=Questrial&family=Carlito:wght@400;700&display=swap">
<style>
  :root{
    --navy:#0c3c69;
    --sky:#2aa7df;
    --paper:#ffffff;
    --backdrop:#e6e8eb;
    --ink:#0c3c69;
    --muted:#44617e;
  }
  *{box-sizing:border-box;margin:0;padding:0}
  html,body{width:1200px;height:1000px;overflow:hidden;background:var(--backdrop)}
  .suite{position:relative;width:1200px;height:1000px;font-family:"Carlito","Calibri",sans-serif;color:var(--ink)}
  .piece{position:absolute;background:var(--paper);box-shadow:0 2px 8px rgba(0,0,0,.18);overflow:hidden}

  /* brand name lockup */
  .brand{position:absolute;display:flex;align-items:center;gap:7px;font-family:"Questrial","Century Gothic",sans-serif;font-weight:400;color:var(--navy);white-space:nowrap}
  .brand--centered{left:0;right:0;justify-content:center}
  .brand__dot{flex:none;border-radius:50%;background:var(--sky)}
  .brand__name{display:flex;flex-direction:column;align-items:center;line-height:1.1}
  .brand__main{letter-spacing:.5px}
  .brand__sub{font-size:.55em;letter-spacing:1.6px}
  .brand--white{color:#fff}
  .brand--white .brand__dot{background:#fff}

  .band{position:absolute;left:0;right:0;bottom:0;background:var(--navy);color:#fff;text-align:center;font-weight:400}
  .label{color:var(--sky)}

  /* letterhead */
  .letterhead{left:38px;top:20px;width:386px;height:543px}
  .letterhead .brand{top:54px}
  .letterhead .brand__dot{width:8px;height:8px}
  .letterhead .brand__name{font-size:15px}
  .letterhead__meta{position:absolute;top:80px;left:0;right:0;text-align:center;font-size:5px;color:var(--muted);line-height:1.45}
  .letterhead__meta .web{font-size:8px;color:var(--navy)}
  .letterhead .band{height:36px;font-size:7.5px;line-height:1.6;padding-top:5px}

  /* business card front, wide */
  .card-wide{left:38px;top:580px;width:440px;height:150px}
  .card-wide .brand{left:30px;top:76px}
  .card-wide .brand__dot{width:8px;height:8px}
  .card-wide .brand__name{font-size:16px}
  .contact{position:absolute;font-size:8px;line-height:1.45;color:var(--muted);white-space:nowrap}
  .contact__name{font-family:"Questrial","Century Gothic",sans-serif;color:var(--navy)}
  .contact__role{color:var(--sky)}
  .card-wide .contact{left:214px;top:26px}
  .card-wide .contact__name{font-size:16px;line-height:1.1}
  .card-wide .contact__role{font-size:8px;margin-bottom:12px}

  /* compliments slip */
  .slip{left:38px;top:765px;width:442px;height:213px}
  .slip__title{position:absolute;left:30px;top:24px;font-family:"Questrial","Century Gothic",sans-serif;font-size:24px;color:var(--navy);font-weight:400}
  .slip .brand{left:302px;top:101px}
  .slip .brand__dot{width:7px;height:7px}
  .slip .brand__name{font-size:14px}
  .slip__details{position:absolute;left:316px;top:128px;font-size:5.2px;line-height:1.5;color:var(--muted)}
  .slip .band{height:32px;font-size:7.5px;line-height:1.4;padding-top:4px}

  /* DL flyer */
  .flyer{left:513px;top:20px;width:295px;height:705px}
  .flyer .brand{top:152px}
  .flyer .brand__dot{width:12px;height:12px}
  .flyer .brand__name{font-size:24px}
  .services{list-style:none;text-align:center;white-space:nowrap}
  .flyer .services{position:absolute;top:280px;left:0;right:0;font-size:15px;line-height:30.5px;color:var(--navy)}
  .flyer .band{height:127px;padding-top:12px}
  .flyer .band .web{font-family:"Questrial","Century Gothic",sans-serif;font-size:16px}
  .flyer .band .tel{font-size:14px;margin-top:4px}

  /* banner */
  .banner{left:843px;top:27px;width:327px;height:680px;background:var(--navy)}
  .banner__scene{position:absolute;left:0;top:0;width:327px;height:534px;background:linear-gradient(180deg,#244f7d 0%,#5a86ad 22%,#9fbcd3 44%,#a9bfcd 52%,#6c8e8f 58%,#3c5a3e 72%,#4c6745 88%,#8a8c87 100%)}
  .banner .brand{top:122px}
  .banner .brand__dot{width:12px;height:12px}
  .banner .brand__name{font-size:25px}
  .banner .services{position:absolute;top:185px;left:0;right:0;font-size:15.5px;line-height:21.7px;color:#fff}
  .banner__footer{position:absolute;top:553px;left:0;right:0;text-align:center;color:#fff}
  .banner__tagline{color:var(--sky);font-size:14px;line-height:21px}
  .banner__web{font-family:"Questrial","Century Gothic",sans-serif;font-size:19px;margin-top:6px}
  .banner__contact{font-size:11px;line-height:15px;margin-top:4px}

  /* business card front, stacked */
  .card-split{left:513px;top:760px;width:327px;height:203px}
  .card-split .brand{left:22px;top:82px}
  .card-split .brand__dot{width:7px;height:7px}
  .card-split .brand__name{font-size:15px}
  .card-split__rule{position:absolute;left:166px;top:50px;width:1px;height:106px;background:var(--sky)}
  .card-split .contact{left:178px;top:72px;font-size:6.5px}
  .card-split .contact__name{font-size:15px;line-height:1.1}
  .card-split .contact__role{font-size:7.5px;margin-bottom:10px}

  /* business card back */
  .card-back{left:857px;top:760px;width:326px;height:203px;background:var(--navy);text-align:center}
  .card-back .brand{top:96px}
  .card-back .brand__dot{width:9px;height:9px}
  .card-back .brand__name{font-size:19px}
  .card-back__web{position:absolute;top:137px;left:0;right:0;font-size:12px;color:var(--sky)}
</style>
</head>
<body>
<main class="suite">

  <!-- Letterhead -->
  <section class="piece letterhead" aria-label="Letterhead">
    <div class="brand brand--centered"><span class="brand__dot"></span><span class="brand__name"><span class="brand__main">KESTREL BAY</span><span class="brand__sub">LAW &amp; SETTLEMENTS</span></span></div>
    <div class="letterhead__meta">
      <div class="web">www.kestrelbaylaw.com.au</div>
      <div>Petra Lusk atf The PJL Family Trust t/as Kestrel Bay Law &amp; Settlements</div>
      <div>ABN 38 402 917 265</div>
    </div>
    <footer class="band">
      <div>Harwood Chambers, Tilbury Lane, Albany &nbsp;&nbsp;&nbsp; <span class="label">Mail</span> PO Box 8127, Albany WA 6332</div>
      <div><span class="label">Telephone</span> 0461 907 352 &nbsp; <span class="label">Facsimile</span> 08 9736 2091 &nbsp; <span class="label">Email</span> info@kestrelbaylaw.com.au</div>
    </footer>
  </section>

  <!-- Business card front, wide layout -->
  <section class="piece card-wide" aria-label="Business card front">
    <div class="brand"><span class="brand__dot"></span><span class="brand__name"><span class="brand__main">KESTREL BAY</span><span class="brand__sub">LAW &amp; SETTLEMENTS</span></span></div>
    <div class="contact">
      <div class="contact__name">Petra Lusk</div>
      <div class="contact__role">Director &amp; Principal Solicitor</div>
      <div>Harwood Chambers, Tilbury Lane, Albany</div>
      <div>PO Box 8127, Albany WA 6332</div>
      <div><span class="label">T</span> 0461 907 352</div>
      <div><span class="label">F</span> 08 9736 2091</div>
      <div>petra@kestrelbaylaw.com.au</div>
    </div>
  </section>

  <!-- With Compliments slip -->
  <section class="piece slip" aria-label="With compliments slip">
    <h1 class="slip__title">With Compliments</h1>
    <div class="brand"><span class="brand__dot"></span><span class="brand__name"><span class="brand__main">KESTREL BAY</span><span class="brand__sub">LAW &amp; SETTLEMENTS</span></span></div>
    <div class="slip__details">
      <div>Harwood Chambers, Tilbury Lane, Albany</div>
      <div><span class="label">Mail</span> PO Box 8127, Albany WA 6332</div>
      <div><span class="label">Telephone</span> 0461 907 352</div>
      <div><span class="label">Facsimile</span> 08 9736 2091</div>
      <div><span class="label">Email</span> info@kestrelbaylaw.com.au</div>
      <div>www.kestrelbaylaw.com.au</div>
    </div>
    <footer class="band">
      <div>Petra Lusk atf The PJL Family Trust t/as Kestrel Bay Law &amp; Settlements</div>
      <div>ABN 38 402 917 265</div>
    </footer>
  </section>

  <!-- DL flyer -->
  <section class="piece flyer" aria-label="DL flyer">
    <div class="brand brand--centered"><span class="brand__dot"></span><span class="brand__name"><span class="brand__main">KESTREL BAY</span><span class="brand__sub">LAW &amp; SETTLEMENTS</span></span></div>
    <ul class="services">
      <li>Wills &amp; Estate Planning</li>
      <li>Probate &amp; Letters of Administration</li>
      <li>Property Law &amp; Conveyancing</li>
      <li>General Commercial Law</li>
      <li>Business Law</li>
    </ul>
    <footer class="band">
      <div class="web">www.kestrelbaylaw.com.au</div>
      <div class="tel"><span class="label">Telephone</span> 0461 907 352</div>
    </footer>
  </section>

  <!-- Banner -->
  <section class="piece banner" aria-label="Event banner">
    <div class="banner__scene" role="img" aria-label="Photograph of Albany harbour and town seen from a bushland hilltop under a blue sky"></div>
    <div class="brand brand--centered brand--white"><span class="brand__dot"></span><span class="brand__name"><span class="brand__main">KESTREL BAY</span><span class="brand__sub">LAW &amp; SETTLEMENTS</span></span></div>
    <ul class="services">
      <li>Wills &amp; Estate Planning</li>
      <li>Probate &amp; Letters of Administration</li>
      <li>Property Law &amp; Conveyancing</li>
      <li>General Commercial Law</li>
      <li>Business Law</li>
    </ul>
    <div class="banner__footer">
      <p class="banner__tagline">Quality Legal Advice and Property<br>Settlements in Albany and the Great Southern</p>
      <p class="banner__web">www.kestrelbaylaw.com.au</p>
      <p class="banner__contact"><span class="label">Telephone</span> 0461 907 352<br><span class="label">Email</span> info@kestrelbaylaw.com.au</p>
    </div>
  </section>

  <!-- Business card front, split layout -->
  <section class="piece card-split" aria-label="Business card front, alternative">
    <div class="brand"><span class="brand__dot"></span><span class="brand__name"><span class="brand__main">KESTREL BAY</span><span class="brand__sub">LAW &amp; SETTLEMENTS</span></span></div>
    <div class="card-split__rule"></div>
    <div class="contact">
      <div class="contact__name">Petra Lusk</div>
      <div class="contact__role">Director &amp; Principal Solicitor</div>
      <div>Harwood Chambers, Tilbury Lane, Albany</div>
      <div>PO Box 8127, Albany WA 6332</div>
      <div><span class="label">T</span> 0461 907 352</div>
      <div><span class="label">F</span> 08 9736 2091</div>
      <div>petra@kestrelbaylaw.com.au</div>
    </div>
  </section>

  <!-- Business card back -->
  <section class="piece card-back" aria-label="Business card back">
    <div class="brand brand--centered brand--white"><span class="brand__dot"></span><span class="brand__name"><span class="brand__main">KESTREL BAY</span><span class="brand__sub">LAW &amp; SETTLEMENTS</span></span></div>
    <div class="card-back__web">www.kestrelbaylaw.com.au</div>
  </section>

</main>
</body>
</html>
```